Master slides for standard ppt presentation

I just my company, went through Quillmarks for the log design and already have an identity that I like.
I need to transpose this identity into some nice Master slides for Powerpoint presentation. I want it clean, with fresh color connection to my logo, not over crowded and obviously different vs what powerpoint proposes as standard design ideas. I will attach a few materials that I already use, branded with the company logo so that you can take inspiration.

```html
<!DOCTYPE html>
<html lang="en">
<head>
<meta charset="utf-8">
<title>Novaridge — Master Slides</title>
<link href="https://fonts.googleapis.com/css2?family=Lexend:wght@300;400;600;700&display=swap" rel="stylesheet">
<style>
:root{
  --green:#0d4f45;
  --green-dark:#083a33;
  --teal:#19b38a;
  --mint:#3fd39e;
  --ink:#1f2b2a;
  --grey:#8c9796;
  --line:#d5dcdb;
  --page:#f4f5f5;
  --photo:linear-gradient(135deg,#c7d0d3,#75868c);
  --city:linear-gradient(180deg,#e9e3cf,#9ba8ab);
}
*{box-sizing:border-box;margin:0;padding:0}
html,body{width:1200px;height:2305px;overflow:hidden;background:var(--page);font-family:"Lexend",sans-serif;color:var(--ink)}
.canvas{position:relative;width:1200px;height:2305px;overflow:hidden}

.hero{position:absolute;left:311px;top:98px;width:578px;height:330px;background:#fff;overflow:hidden;box-shadow:0 6px 24px rgba(0,0,0,.12)}
.hero-bg{position:absolute;inset:0;background:linear-gradient(90deg,#fff 40%,#eef1f1)}
.hero-photo{position:absolute;left:258px;top:70px;width:330px;height:200px;border-radius:50%;background:var(--city)}
.brand{display:flex;align-items:center;justify-content:center;gap:6px;color:var(--green);font-weight:700;letter-spacing:.02em}
.brand i{display:block;background:linear-gradient(180deg,var(--mint),var(--green))}
.hero .brand{position:absolute;left:40px;top:70px;width:170px;font-size:14px}
.hero .brand i{width:22px;height:22px}
.hero h1{position:absolute;left:20px;top:138px;width:210px;text-align:center;font-size:21px;font-weight:600;line-height:1.3;color:var(--green)}
.hero .rule{position:absolute;left:30px;top:204px;width:190px;height:1px;background:var(--teal)}
.hero .sub{position:absolute;left:20px;top:212px;width:210px;text-align:center;font-size:11px;font-weight:300;color:var(--green);line-height:1.25}
.dots{position:absolute;display:flex;gap:7px}
.dots span{display:block;border-radius:50%;background:var(--green)}
.hero .dots{left:100px;top:282px}
.hero .dots span{width:18px;height:18px}
.hero-foot{position:absolute;left:0;right:0;bottom:0;height:20px;background:var(--green);color:#fff;font-size:7.5px;font-weight:300;text-align:center;line-height:20px}

.deck{position:absolute;left:81px;top:558px;display:grid;grid-template-columns:repeat(4,238px);column-gap:29px;row-gap:22px}
.slide{position:relative;width:238px;height:133px;background:#fff;overflow:hidden;box-shadow:0 2px 8px rgba(0,0,0,.08)}
.std::after{content:"";position:absolute;left:18px;right:6px;bottom:5px;height:3px;background:var(--green)}
.std::before{content:"";position:absolute;left:5px;bottom:4px;width:9px;height:6px;background:linear-gradient(180deg,var(--mint),var(--green))}
.st{position:absolute;left:12px;top:9px;font-size:5.6px;font-weight:700;color:var(--ink);letter-spacing:.03em;text-transform:uppercase}
.st b{color:var(--teal)}
.ph{position:absolute;background:var(--photo)}
.ph.city{background:var(--city)}
.p{position:absolute;font-size:3.4px;line-height:1.5;color:var(--grey);font-weight:300;text-align:justify}
.p.c{text-align:center}
.p.r{text-align:right}
.gbox{position:absolute;background:var(--green);color:#fff}
.gbox .h{font-size:4.5px;font-weight:600}
.gbox .p{position:static;color:#cfe3df}
.lbl{font-size:4.6px;font-weight:600;color:var(--green);text-transform:uppercase}

.cover .brand{position:absolute;font-size:7px}
.cover h2{position:absolute;font-size:8.5px;font-weight:600;line-height:1.3;text-align:center;color:var(--green)}
.cover .cs{position:absolute;font-size:4px;text-align:center;color:var(--green);font-weight:300;line-height:1.3}
.cover .dots span{width:6px;height:6px}
.cover .cfoot{position:absolute;left:0;right:0;bottom:0;height:5px;background:var(--green)}
.cover.dark{background:var(--green)}
.cover.dark .brand,.cover.dark h2,.cover.dark .cs{color:#fff}
.cover.dark .dots span{background:#fff}
.cover.dark .cfoot{background:var(--green-dark)}

.agenda-list{position:absolute;left:138px;top:22px;width:88px;list-style:none}
.agenda-list li{font-size:4.3px;color:var(--grey);border-bottom:.5px solid var(--teal);padding:2px 0 2.6px 3px;font-weight:300}

.stat{display:inline-block;width:48%;text-align:center}
.stat b{display:block;font-size:8px}
.stat small{font-size:3px;color:#cfe3df}

.card{position:absolute;background:#fff;box-shadow:0 1px 4px rgba(0,0,0,.12)}
.ico{position:absolute;width:11px;height:11px;border:.6px solid var(--line);border-radius:2px;box-shadow:0 1px 2px rgba(0,0,0,.1)}
.ico::after{content:"";position:absolute;left:3px;top:3px;width:5px;height:5px;border:.8px solid var(--green);border-radius:1px}

.team{position:absolute;top:40px;width:58px;height:85px;background:var(--green);text-align:center;color:#fff}
.team .av{position:absolute;left:14px;top:-14px;width:30px;height:30px;border-radius:50%;background:var(--photo);border:2px solid #fff}
.team .p{position:absolute;left:6px;right:6px;top:22px;color:#cfe3df;text-align:center}
.team .nm{position:absolute;left:0;right:0;bottom:5px;font-size:3.8px;font-weight:600;letter-spacing:.05em}

.vlabel{position:absolute;left:4px;top:30px;width:10px;height:80px;writing-mode:vertical-rl;transform:rotate(180deg);font-size:5px;font-weight:700;color:var(--ink);text-align:center}

.price{position:absolute;top:28px;width:40px;height:90px;background:#fff;box-shadow:0 1px 4px rgba(0,0,0,.15);text-align:center}
.price .n{font-size:4.3px;color:var(--ink);margin-top:5px}
.price .v{background:var(--green);color:#fff;font-size:7px;margin:4px 0;padding:4px 0}
.price .f{font-size:3px;color:var(--grey);line-height:1.8}
.price .btn{display:inline-block;margin-top:5px;background:var(--ink);color:#fff;font-size:2.8px;padding:1.5px 5px}

.tbl{position:absolute;left:20px;top:34px;width:198px;border-collapse:collapse;font-size:3.4px;color:var(--grey)}
.tbl th{background:var(--green);color:#fff;font-weight:600;font-size:4.5px;padding:2px}
.tbl td{border-bottom:.5px solid var(--line);padding:2.6px 3px;text-align:center}
.tbl td:first-child{text-align:left}

.client{position:absolute;width:26px;height:12px;background:#fff;box-shadow:0 1px 3px rgba(0,0,0,.15);font-size:3.6px;color:var(--ink);display:flex;align-items:center;justify-content:center;gap:1.5px}
.client i{width:3px;height:3px;background:var(--grey)}

.tcard{position:absolute;top:30px;width:52px;height:78px;background:#fff;box-shadow:0 1px 4px rgba(0,0,0,.15);text-align:center}
.tcard.on{background:#7c8483;height:88px;top:25px}
.tcard .av{width:16px;height:16px;margin:10px auto 3px;background:var(--photo)}
.tcard .stars{font-size:4px;color:#e7b416}
.tcard .p{position:static;margin:2px 5px;text-align:center}
.tcard .nm{font-size:3.6px;color:var(--teal);font-weight:600}
.tcard.on .p,.tcard.on .nm{color:#fff}

.iconset{position:absolute;left:10px;right:10px;text-align:center;color:#9aa3a2;font-size:5.2px;letter-spacing:2.2px;line-height:1.6;word-break:break-all}
.iconset h4{font-size:5.2px;font-weight:400;color:var(--ink);letter-spacing:0;margin:3px 0 1px}

.thanks{background:linear-gradient(180deg,#e9efee 0%,#a9bab7 45%,var(--green) 100%)}
.thanks .brand{position:absolute;left:0;right:0;top:28px;font-size:8px}
.thanks h3{position:absolute;left:0;right:0;top:70px;text-align:center;color:#fff;font-size:19px;font-weight:400}
</style>
</head>
<body>
<main class="canvas">

  <section class="hero">
    <div class="hero-bg"></div>
    <div class="hero-photo" role="img" aria-label="City skyline photograph in warm mist"></div>
    <div class="brand"><i></i>NOVARIDGE</div>
    <h1>Presentation Title<br>Goes Here</h1>
    <div class="rule"></div>
    <p class="sub">Credential Subtitle<br>Presentation</p>
    <div class="dots"><span></span><span></span><span></span><span></span></div>
    <footer class="hero-foot">Copyright © 2023 NOVARIDGE. All rights reserved.</footer>
  </section>

  <section class="deck">

    <article class="slide cover">
      <div class="ph city" style="inset:0;opacity:.55" role="img" aria-label="Faded city skyline background"></div>
      <div class="brand" style="left:64px;top:18px;width:110px">NOVARIDGE</div>
      <h2 style="left:64px;top:68px;width:110px">Presentation Title<br>Goes Here</h2>
      <p class="cs" style="left:64px;top:96px;width:110px">Credential Subtitle<br>Presentation</p>
      <div class="dots" style="left:99px;top:113px"><span></span><span></span><span></span><span></span></div>
      <div class="cfoot"></div>
    </article>

    <article class="slide cover dark">
      <div class="ph city" style="left:100px;top:20px;width:150px;height:95px;border-radius:50%" role="img" aria-label="City skyline photograph"></div>
      <div class="brand" style="left:4px;top:22px;width:100px">NOVARIDGE</div>
      <h2 style="left:4px;top:58px;width:100px">Presentation Title<br>Goes Here</h2>
      <p class="cs" style="left:4px;top:83px;width:100px">Credential Subtitle<br>Presentation</p>
      <div class="dots" style="left:30px;top:112px"><span></span><span></span><span></span><span></span></div>
      <div class="cfoot"></div>
    </article>

    <article class="slide cover">
      <div class="ph city" style="left:100px;top:20px;width:150px;height:95px;border-radius:50%" role="img" aria-label="City skyline photograph"></div>
      <div class="brand" style="left:4px;top:22px;width:100px">NOVARIDGE</div>
      <h2 style="left:4px;top:58px;width:100px">Presentation Title<br>Goes Here</h2>
      <p class="cs" style="left:4px;top:83px;width:100px">Credential Subtitle<br>Presentation</p>
      <div class="dots" style="left:30px;top:112px"><span></span><span></span><span></span><span></span></div>
      <div class="cfoot"></div>
    </article>

    <article class="slide std">
      <div class="gbox" style="left:0;top:0;width:52px;height:116px"><div class="h" style="position:absolute;left:9px;top:58px;font-size:6.5px">AGENDA</div></div>
      <div class="ph" style="left:52px;top:0;width:70px;height:116px" role="img" aria-label="Portrait photo of a businessman in a suit"></div>
      <ul class="agenda-list">
        <li>Table of content</li><li>About Us</li><li>Tender Overview</li><li>Our Services</li><li>Our Team</li><li>Contact us</li>
      </ul>
    </article>

    <article class="slide std">
      <div class="st">About <b>Us</b></div>
      <div class="ph" style="left:150px;top:0;width:88px;height:55px" role="img" aria-label="Business team meeting photo"></div>
      <div class="gbox" style="left:30px;top:30px;width:140px;height:26px;padding-top:5px">
        <span class="stat"><b>10+</b><small>Year Of Excellence</small></span><span class="stat"><b>240+</b><small>Projects Done</small></span>
      </div>
      <p class="p" style="left:24px;top:66px;width:88px">Our team plans each project with care, from the first brief to the final review. We listen closely, set clear goals and share progress at every step, so clients always know where things stand and what comes next. We listen closely, set clear goals and share progress at every step.</p>
      <p class="p" style="left:126px;top:66px;width:88px">Our team plans each project with care, from the first brief to the final review. We listen closely, set clear goals and share progress at every step, so clients always know where things stand and what comes next. We listen closely, set clear goals and share progress at every step.</p>
    </article>

    <article class="slide std">
      <div class="st">Our <b>History</b></div>
      <p class="p" style="left:14px;top:22px;width:100px">Our team plans each project with care, from the first brief to the final review. We listen closely, set clear goals and share progress at every step, so clients always know where things stand and what comes next. Our team plans each project with care, from the first brief to the final review. We listen closely, set clear goals and share progress at every step, so clients always know where things stand and what comes next.</p>
      <p class="p" style="left:14px;top:70px;width:100px">Our team plans each project with care, from the first brief to the final review. We listen closely, set clear goals and share progress at every step, so clients always know where things stand and what comes next. We listen closely, set clear goals and share progress at every step.</p>
      <div class="ph" style="left:122px;top:36px;width:80px;height:82px" role="img" aria-label="Two colleagues talking in an office"></div>
      <div class="gbox" style="left:172px;top:20px;width:66px;height:28px;padding:5px 8px"><div class="h">Happy Clients</div><p class="p">Client note goes here</p></div>
    </article>

    <article class="slide std">
      <div class="st">Why are <b>we here?</b></div>
      <div class="ph" style="left:24px;top:20px;width:95px;height:64px" role="img" aria-label="Business people reviewing documents"></div>
      <div class="gbox" style="left:110px;top:28px;width:128px;height:48px;padding:10px 14px"><p class="p">Our team plans each project with care, from the first brief to the final review. We listen closely, set clear goals and share progress at every step, so clients always know where things stand and what comes next.</p></div>
      <p class="p" style="left:24px;top:90px;width:200px">Our team plans each project with care, from the first brief to the final review. We listen closely, set clear goals and share progress at every step, so clients always know where things stand and what comes next. We listen closely, set clear goals and share progress at every step.</p>
    </article>

    <article class="slide std">
      <div class="st">Why you should <b>choose us?</b></div>
      <p class="p" style="left:24px;top:24px;width:96px">Our team plans each project with care, from the first brief to the final review. We listen closely, set clear goals and share progress at every step, so clients always know where things stand and what comes next.</p>
      <p class="p" style="left:24px;top:54px;width:96px">We listen closely, set clear goals and share progress at every step.</p>
      <p class="p" style="left:130px;top:24px;width:96px">Our team plans each project with care, from the first brief to the final review. We listen closely, set clear goals and share progress at every step, so clients always know where things stand and what comes next.</p>
      <div class="ph" style="left:140px;top:62px;width:98px;height:56px" role="img" aria-label="Team working at a laptop"></div>
      <div class="gbox" style="left:26px;top:84px;width:130px;height:22px;padding:4px 10px"><div class="h" style="font-weight:300">Get Reward</div><p class="p">We listen closely and set clear goals.</p></div>
    </article>

    <article class="slide std">
      <div class="st">Our great <b>vision</b></div>
      <div class="ph" style="left:20px;top:36px;width:76px;height:70px" role="img" aria-label="Hands pointing at a printed chart"></div>
      <p class="p" style="left:108px;top:30px;width:120px">Our team plans each project with care, from the first brief to the final review. We listen closely, set clear goals and share progress at every step, so clients always know where things stand and what comes next.</p>
      <div class="gbox" style="left:108px;top:58px;width:56px;height:22px;padding:4px 6px"><div class="h" style="font-weight:300">Unique Text</div><p class="p">Short note goes here</p></div>
      <div class="gbox" style="left:168px;top:58px;width:56px;height:22px;padding:4px 6px"><div class="h" style="font-weight:300">Unique Text</div><p class="p">Short note goes here</p></div>
      <p class="p" style="left:108px;top:85px;width:120px">Our team plans each project with care, from the first brief to the final review. We listen closely, set clear goals and share progress at every step, so clients always know where things stand and what comes next.</p>
    </article>

    <article class="slide std">
      <div class="st">Our <b>services/work</b></div>
      <div class="card" style="left:40px;top:28px;width:52px;height:88px"><div class="ph" style="left:0;top:0;width:52px;height:28px" role="img" aria-label="Office meeting photo"></div><div class="lbl" style="position:absolute;top:31px;width:100%;text-align:center;font-size:3.6px">Service One</div><p class="p c" style="left:5px;top:38px;width:42px">Our team plans each project with care, from the first brief to the final review. We listen closely, set clear goals and share progress at every step, so clients always know where things stand and what comes next.</p></div>
      <div class="card" style="left:100px;top:28px;width:52px;height:88px"><div class="ph city" style="left:0;top:0;width:52px;height:28px" role="img" aria-label="City towers photo"></div><div class="lbl" style="position:absolute;top:31px;width:100%;text-align:center;font-size:3.6px">Service Two</div><p class="p c" style="left:5px;top:38px;width:42px">Our team plans each project with care, from the first brief to the final review. We listen closely, set clear goals and share progress at every step, so clients always know where things stand and what comes next.</p></div>
      <div class="card" style="left:160px;top:28px;width:52px;height:88px"><div class="ph" style="left:0;top:0;width:52px;height:28px" role="img" aria-label="Handshake photo"></div><div class="lbl" style="position:absolute;top:31px;width:100%;text-align:center;font-size:3.6px">Service Three</div><p class="p c" style="left:5px;top:38px;width:42px">Our team plans each project with care, from the first brief to the final review. We listen closely, set clear goals and share progress at every step, so clients always know where things stand and what comes next.</p></div>
    </article>

    <article class="slide std">
      <div class="st">Our <b>value</b></div>
      <div class="ico" style="left:30px;top:34px"></div><div class="lbl" style="position:absolute;left:48px;top:30px;text-transform:none;font-size:3.8px">Content here</div><p class="p" style="left:48px;top:36px;width:62px">We listen closely, set clear goals and share progress at every step.</p>
      <div class="ico" style="left:30px;top:62px"></div><div class="lbl" style="position:absolute;left:48px;top:58px;text-transform:none;font-size:3.8px">Content here</div><p class="p" style="left:48px;top:64px;width:62px">We listen closely, set clear goals and share progress at every step.</p>
      <div class="ico" style="left:30px;top:90px"></div><div class="lbl" style="position:absolute;left:48px;top:86px;text-transform:none;font-size:3.8px">Content here</div><p class="p" style="left:48px;top:92px;width:62px">We listen closely, set clear goals and share progress at every step.</p>
      <div class="ico" style="left:122px;top:34px"></div><div class="lbl" style="position:absolute;left:140px;top:30px;text-transform:none;font-size:3.8px">Content here</div><p class="p" style="left:140px;top:36px;width:62px">We listen closely, set clear goals and share progress at every step.</p>
      <div class="ico" style="left:122px;top:62px"></div><div class="lbl" style="position:absolute;left:140px;top:58px;text-transform:none;font-size:3.8px">Content here</div><p class="p" style="left:140px;top:64px;width:62px">We listen closely, set clear goals and share progress at every step.</p>
      <div class="ico" style="left:122px;top:90px"></div><div class="lbl" style="position:absolute;left:140px;top:86px;text-transform:none;font-size:3.8px">Content here</div><p class="p" style="left:140px;top:92px;width:62px">We listen closely, set clear goals and share progress at every step.</p>
    </article>

    <article class="slide std">
      <div class="st">Our <b>team</b></div>
      <div class="team" style="left:30px"><div class="av" role="img" aria-label="Team member portrait"></div><p class="p">We listen closely, set clear goals and share progress at every step.</p><div class="nm">Mara Ellison</div></div>
      <div class="team" style="left:98px"><div class="av" role="img" aria-label="Team member portrait"></div><p class="p">We listen closely, set clear goals and share progress at every step.</p><div class="nm">Owen Pratt</div></div>
      <div class="team" style="left:166px"><div class="av" role="img" aria-label="Team member portrait"></div><p class="p">We listen closely, set clear goals and share progress at every step.</p><div class="nm">Luca Farrow</div></div>
    </article>

    <article class="slide std">
      <div class="st">Cover <b>sheet</b></div>
      <p class="p" style="left:14px;top:22px;width:104px">Our team plans each project with care, from the first brief to the final review. We listen closely, set clear goals and share progress at every step, so clients always know where things stand and what comes next. Our team plans each project with care, from the first brief to the final review. We listen closely, set clear goals and share progress at every step, so clients always know where things stand and what comes next.</p>
      <p class="p" style="left:14px;top:66px;width:104px">Our team plans each project with care, from the first brief to the final review. We listen closely, set clear goals and share progress at every step, so clients always know where things stand and what comes next.</p>
      <div class="ph" style="left:125px;top:24px;width:98px;height:96px;background:linear-gradient(135deg,#5c6566,#aab3b4)" role="img" aria-label="Mosaic of portrait photographs"></div>
      <div class="gbox" style="left:72px;top:96px;width:70px;height:18px;padding:3px 8px"><div class="h" style="font-weight:300">Theo Marlin</div><p class="p">Project lead</p></div>
    </article>

    <article class="slide std">
      <div class="st">Two text <b>columns</b></div>
      <p class="p" style="left:22px;top:28px;width:95px">Our team plans each project with care, from the first brief to the final review. We listen closely, set clear goals and share progress at every step, so clients always know where things stand and what comes next. Our team plans each project with care, from the first brief to the final review. We listen closely, set clear goals and share progress at every step, so clients always know where things stand and what comes next. Our team plans each project with care, from the first brief to the final review. We listen closely, set clear goals and share progress at every step, so clients always know where things stand and what comes next.</p>
      <p class="p" style="left:126px;top:28px;width:95px">Our team plans each project with care, from the first brief to the final review. We listen closely, set clear goals and share progress at every step, so clients always know where things stand and what comes next. Our team plans each project with care, from the first brief to the final review. We listen closely, set clear goals and share progress at every step, so clients always know where things stand and what comes next. Our team plans each project with care, from the first brief to the final review. We listen closely, set clear goals and share progress at every step, so clients always know where things stand and what comes next.</p>
      <div class="gbox" style="left:196px;top:6px;width:42px;height:18px;padding:3px 5px"><div class="h" style="font-size:3.6px">Happy Clients</div><p class="p">Short note here</p></div>
    </article>

    <article class="slide std">
      <div class="st">Two text <b>columns</b></div>
      <p class="p" style="left:22px;top:24px;width:205px">Our team plans each project with care, from the first brief to the final review. We listen closely, set clear goals and share progress at every step, so clients always know where things stand and what comes next. Our team plans each project with care, from the first brief to the final review. We listen closely, set clear goals and share progress at every step, so clients always know where things stand and what comes next. Our team plans each project with care, from the first brief to the final review. We listen closely, set clear goals and share progress at every step, so clients always know where things stand and what comes next.</p>
      <p class="p" style="left:22px;top:62px;width:205px">Our team plans each project with care, from the first brief to the final review. We listen closely, set clear goals and share progress at every step, so clients always know where things stand and what comes next. Our team plans each project with care, from the first brief to the final review. We listen closely, set clear goals and share progress at every step, so clients always know where things stand and what comes next. Our team plans each project with care, from the first brief to the final review. We listen closely, set clear goals and share progress at every step, so clients always know where things stand and what comes next.</p>
      <div class="gbox" style="left:134px;top:104px;width:104px;height:18px;padding:3px 8px"><div class="h" style="font-size:3.6px;font-weight:300">Happy Clients</div><p class="p">Short note goes here</p></div>
    </article>

    <article class="slide std">
      <div class="st">Three text <b>columns</b></div>
      <p class="p" style="left:22px;top:24px;width:60px">Our team plans each project with care, from the first brief to the final review. We listen closely, set clear goals and share progress at every step, so clients always know where things stand and what comes next. Our team plans each project with care, from the first brief to the final review. We listen closely, set clear goals and share progress at every step, so clients always know where things stand and what comes next. We listen closely, set clear goals and share progress at every step.</p>
      <p class="p" style="left:88px;top:24px;width:60px">Our team plans each project with care, from the first brief to the final review. We listen closely, set clear goals and share progress at every step, so clients always know where things stand and what comes next. Our team plans each project with care, from the first brief to the final review. We listen closely, set clear goals and share progress at every step, so clients always know where things stand and what comes next. We listen closely, set clear goals and share progress at every step.</p>
      <p class="p" style="left:154px;top:24px;width:60px">Our team plans each project with care, from the first brief to the final review. We listen closely, set clear goals and share progress at every step, so clients always know where things stand and what comes next. Our team plans each project with care, from the first brief to the final review. We listen closely, set clear goals and share progress at every step, so clients always know where things stand and what comes next. We listen closely, set clear goals and share progress at every step.</p>
      <div class="gbox" style="left:224px;top:0;width:14px;height:100px"></div>
    </article>

    <article class="slide std">
      <div class="st">Text and picture <b>slide</b></div>
      <p class="p" style="left:14px;top:22px;width:112px">Our team plans each project with care, from the first brief to the final review. We listen closely, set clear goals and share progress at every step, so clients always know where things stand and what comes next. Our team plans each project with care, from the first brief to the final review. We listen closely, set clear goals and share progress at every step, so clients always know where things stand and what comes next.</p>
      <p class="p" style="left:14px;top:66px;width:104px">Our team plans each project with care, from the first brief to the final review. We listen closely, set clear goals and share progress at every step, so clients always know where things stand and what comes next. We listen closely, set clear goals and share progress at every step.</p>
      <div class="ph" style="left:134px;top:22px;width:104px;height:96px" role="img" aria-label="Hands pointing at a printed chart"></div>
      <div class="gbox" style="left:124px;top:100px;width:56px;height:18px;padding:3px 6px"><div class="h" style="font-size:3.6px;font-weight:300">Happy Clients</div><p class="p">Short note here</p></div>
    </article>

    <article class="slide std">
      <div class="vlabel">IMAGE GALLERY</div>
      <div class="ph" style="left:18px;top:10px;width:58px;height:52px" role="img" aria-label="Team meeting photo"></div>
      <div class="ph" style="left:80px;top:10px;width:50px;height:52px" role="img" aria-label="Colleagues at a desk photo"></div>
      <div class="gbox" style="left:134px;top:10px;width:56px;height:52px;padding:18px 6px 0"><div class="h" style="font-size:3.4px;letter-spacing:.1em">SERVICE NAME</div><p class="p">We listen closely, set clear goals and share progress at every step.</p></div>
      <div class="ph" style="left:194px;top:10px;width:36px;height:52px" role="img" aria-label="Businessman portrait"></div>
      <div class="ph" style="left:18px;top:66px;width:58px;height:50px" role="img" aria-label="Office workers photo"></div>
      <div class="ph" style="left:80px;top:66px;width:50px;height:50px" role="img" aria-label="Meeting room photo"></div>
      <div class="ph" style="left:134px;top:66px;width:36px;height:50px" role="img" aria-label="Handshake photo"></div>
      <div class="ph" style="left:174px;top:66px;width:56px;height:50px" role="img" aria-label="Business presentation photo"></div>
    </article>

    <article class="slide std">
      <div class="vlabel">IMAGE GALLERY</div>
      <div class="ph" style="left:18px;top:10px;width:96px;height:52px" role="img" aria-label="Two colleagues reviewing work"></div>
      <div class="ph" style="left:118px;top:10px;width:72px;height:52px;background:linear-gradient(135deg,#2b2a27,#9b7b4a)" role="img" aria-label="Glowing light bulb in hand"></div>
      <div class="gbox" style="left:194px;top:10px;width:36px;height:52px"></div>
      <div class="gbox" style="left:18px;top:66px;width:64px;height:50px;padding:14px 6px 0"><div class="h" style="font-size:3.4px;letter-spacing:.1em">SERVICE NAME</div><p class="p">We listen closely, set clear goals and share progress at every step.</p></div>
      <div class="ph" style="left:86px;top:66px;width:56px;height:50px" role="img" aria-label="Businessman portrait"></div>
      <div class="gbox" style="left:146px;top:66px;width:40px;height:50px"></div>
      <div class="ph" style="left:190px;top:66px;width:40px;height:50px" role="img" aria-label="Team at a table"></div>
    </article>

    <article class="slide std">
      <div class="st">Image <b>gallery</b></div>
      <div class="ph" style="left:22px;top:26px;width:66px;height:86px" role="img" aria-label="Team working in an office"></div>
      <div class="ph" style="left:92px;top:26px;width:66px;height:48px;background:linear-gradient(135deg,#1c2a33,#4f7180)" role="img" aria-label="Growth arrow concept photo"></div>
      <div class="gbox" style="left:92px;top:78px;width:66px;height:22px;padding:4px 6px"><p class="p">We listen closely, set clear goals and share progress at every step.</p></div>
      <p class="p" style="left:166px;top:24px;width:64px">Our team plans each project with care, from the first brief to the final review. We listen closely, set clear goals and share progress at every step, so clients always know where things stand and what comes next. Our team plans each project with care, from the first brief to the final review. We listen closely, set clear goals and share progress at every step, so clients always know where things stand and what comes next.</p>
    </article>

    <article class="slide std">
      <div class="st">Pricing <b>tables</b></div>
      <div class="price" style="left:48px"><div class="n">Comfort</div><div class="v">$750</div><div class="f">Feature item<br>Feature item<br>Feature item</div><span class="btn">Book Now</span></div>
      <div class="price" style="left:99px;top:22px;height:96px"><div class="n">Premium</div><div class="v" style="padding:6px 0">$899</div><div class="f">Feature item<br>Feature item<br>Feature item</div><span class="btn">Book Now</span></div>
      <div class="price" style="left:150px"><div class="n">Business</div><div class="v">$850</div><div class="f">Feature item<br>Feature item<br>Feature item</div><span class="btn">Book Now</span></div>
    </article>

    <article class="slide std">
      <div class="st" style="font-weight:400">Process <b>slide</b></div>
      <svg style="position:absolute;left:0;top:0" width="238" height="133" viewBox="0 0 238 133">
        <line x1="14" y1="73" x2="228" y2="73" stroke="#1f2b2a" stroke-width=".8"/>
        <g fill="#fff" stroke="#0d4f45" stroke-width="1">
          <circle cx="38" cy="73" r="5"/><circle cx="72" cy="73" r="5"/><circle cx="106" cy="73" r="5"/><circle cx="140" cy="73" r="5"/><circle cx="174" cy="73" r="5"/><circle cx="208" cy="73" r="5"/>
        </g>
        <g font-size="4" text-anchor="middle" fill="#1f2b2a" font-family="Lexend">
          <text x="38" y="74.5">01</text><text x="72" y="74.5">02</text><text x="106" y="74.5">03</text><text x="140" y="74.5">04</text><text x="174" y="74.5">05</text><text x="208" y="74.5">06</text>
        </g>
        <g stroke="#8c9796" stroke-width=".5" stroke-dasharray="1 1">
          <line x1="72" y1="48" x2="72" y2="66"/><line x1="140" y1="48" x2="140" y2="66"/><line x1="208" y1="48" x2="208" y2="66"/>
          <line x1="38" y1="80" x2="38" y2="98"/><line x1="106" y1="80" x2="106" y2="98"/><line x1="174" y1="80" x2="174" y2="98"/>
        </g>
        <g font-size="3.4" text-anchor="middle" fill="#0d4f45" font-family="Lexend">
          <text x="72" y="30">Content</text><text x="140" y="30">Content</text><text x="208" y="30">Content</text>
          <text x="38" y="103">Content</text><text x="106" y="103">Content</text><text x="174" y="103">Content</text>
        </g>
        <g font-size="2.6" text-anchor="middle" fill="#8c9796" font-family="Lexend">
          <text x="72" y="36">Set clear goals</text><text x="72" y="40">at every step.</text>
          <text x="140" y="36">Set clear goals</text><text x="140" y="40">at every step.</text>
          <text x="208" y="36">Set clear goals</text><text x="208" y="40">at every step.</text>
          <text x="38" y="109">Set clear goals</text><text x="38" y="113">at every step.</text>
          <text x="106" y="109">Set clear goals</text><text x="106" y="113">at every step.</text>
          <text x="174" y="109">Set clear goals</text><text x="174" y="113">at every step.</text>
        </g>
      </svg>
    </article>

    <article class="slide std">
      <div class="st" style="font-weight:400">Process <b>slide</b></div>
      <svg style="position:absolute;left:0;top:0" width="238" height="133" viewBox="0 0 238 133">
        <circle cx="35" cy="68" r="9" fill="#fff" stroke="#0d4f45" stroke-width="1.5"/>
        <circle cx="72" cy="68" r="7" fill="#fff" stroke="#0d4f45" stroke-width="1.5"/>
        <line x1="44" y1="68" x2="65" y2="68" stroke="#1f2b2a" stroke-width=".5"/>
        <line x1="79" y1="68" x2="106" y2="68" stroke="#1f2b2a" stroke-width=".5"/>
        <rect x="106" y="24" width="14" height="92" rx="7" fill="#1f2b2a"/>
        <g fill="#fff" stroke="#0d4f45"><circle cx="113" cy="35" r="5"/><circle cx="113" cy="68" r="5"/><circle cx="113" cy="104" r="5"/></g>
        <line x1="120" y1="48" x2="142" y2="48" stroke="#1f2b2a" stroke-width=".5"/>
        <rect x="142" y="41" width="12" height="12" transform="rotate(45 148 47)" fill="#fff" stroke="#1f2b2a"/>
        <line x1="155" y1="47" x2="198" y2="47" stroke="#1f2b2a" stroke-width=".5"/>
        <line x1="120" y1="104" x2="198" y2="104" stroke="#1f2b2a" stroke-width=".5"/>
        <rect x="190" y="41" width="40" height="12" rx="6" fill="#3fd39e"/>
        <rect x="190" y="98" width="40" height="12" rx="6" fill="#3fd39e"/>
        <circle cx="190" cy="47" r="5" fill="#fff" stroke="#0d4f45"/><circle cx="190" cy="104" r="5" fill="#fff" stroke="#0d4f45"/>
        <g font-size="3.2" fill="#1f2b2a" font-family="Lexend" text-anchor="middle">
          <text x="35" y="84">Project Title</text><text x="72" y="82">Process</text><text x="113" y="20">Option 1</text>
          <text x="210" y="48.5" fill="#fff">Result 1</text><text x="210" y="105.5" fill="#fff">Result 2</text>
        </g>
        <g font-size="2.6" fill="#8c9796" font-family="Lexend" text-anchor="middle"><text x="72" y="87">Set clear goals</text><text x="72" y="91">at every step.</text></g>
      </svg>
    </article>

    <article class="slide std">
      <div class="st">Data driven <b>chart slide</b></div>
      <p class="p" style="left:14px;top:22px;width:72px">Our team plans each project with care, from the first brief to the final review. We listen closely, set clear goals and share progress at every step, so clients always know where things stand and what comes next.</p>
      <p class="p" style="left:14px;top:60px;width:72px">Our team plans each project with care, from the first brief to the final review. We listen closely, set clear goals and share progress at every step, so clients always know where things stand and what comes next. We listen closely, set clear goals and share progress at every step.</p>
      <svg style="position:absolute;left:92px;top:26px" width="146" height="90" viewBox="0 0 146 90">
        <rect x="2" y="2" width="104" height="74" rx="2" fill="#1f2b2a"/>
        <rect x="6" y="6" width="96" height="66" fill="#fff"/>
        <rect x="-6" y="76" width="120" height="4" rx="2" fill="#c7cccc"/>
        <g fill="#19b38a">
          <rect x="18" y="36" width="3" height="26"/><rect x="23" y="44" width="3" height="18"/><rect x="28" y="28" width="3" height="34"/>
          <rect x="40" y="40" width="3" height="22"/><rect x="45" y="30" width="3" height="32"/><rect x="50" y="48" width="3" height="14"/>
          <rect x="62" y="34" width="3" height="28"/><rect x="67" y="22" width="3" height="40"/><rect x="72" y="44" width="3" height="18"/>
          <rect x="84" y="30" width="3" height="32"/><rect x="89" y="40" width="3" height="22"/><rect x="94" y="24" width="3" height="38"/>
        </g>
        <line x1="12" y1="62" x2="100" y2="62" stroke="#1f2b2a" stroke-width=".4"/>
        <g font-size="3" fill="#8c9796" font-family="Lexend" text-anchor="middle"><text x="24" y="67">2016</text><text x="46" y="67">2017</text><text x="68" y="67">2018</text><text x="90" y="67">2019</text></g>
        <g fill="#0d4f45"><rect x="110" y="14" width="30" height="8" rx="4"/><rect x="110" y="34" width="30" height="8" rx="4"/><rect x="110" y="54" width="30" height="8" rx="4"/></g>
      </svg>
    </article>

    <article class="slide std">
      <div class="st">Data driven <b>pie charts</b></div>
      <p class="p c" style="left:14px;top:18px;width:210px;color:#1f2b2a">Our team plans each project with care, from the first brief to the final review. We listen closely, set clear goals and share progress at every step, so clients always know where things stand and what comes next.</p>
      <svg style="position:absolute;left:0;top:0" width="238" height="133" viewBox="0 0 238 133">
        <g fill="none" stroke-width="4">
          <circle cx="52" cy="70" r="13" stroke="#e3e7e7"/><circle cx="52" cy="70" r="13" stroke="#0d4f45" stroke-dasharray="61.3 81.7" transform="rotate(-90 52 70)"/>
          <circle cx="118" cy="70" r="13" stroke="#e3e7e7"/><circle cx="118" cy="70" r="13" stroke="#0d4f45" stroke-dasharray="69.4 81.7" transform="rotate(-90 118 70)"/>
          <circle cx="184" cy="70" r="13" stroke="#e3e7e7"/><circle cx="184" cy="70" r="13" stroke="#0d4f45" stroke-dasharray="44.9 81.7" transform="rotate(-90 184 70)"/>
        </g>
        <g font-size="6" font-weight="600" fill="#1f2b2a" font-family="Lexend" text-anchor="middle"><text x="52" y="72">75%</text><text x="118" y="72">85%</text><text x="184" y="72">55%</text></g>
      </svg>
      <p class="p c" style="left:30px;top:90px;width:44px">We listen closely, set clear goals and share progress at every step.</p>
      <p class="p c" style="left:96px;top:90px;width:44px">We listen closely, set clear goals and share progress at every step.</p>
      <p class="p c" style="left:162px;top:90px;width:44px">We listen closely, set clear goals and share progress at every step.</p>
    </article>

    <article class="slide std">
      <div class="st" style="font-weight:400">Data driven line <b>chart</b></div>
      <div class="gbox" style="left:14px;top:24px;width:122px;height:7px;font-size:4px;text-align:center;line-height:7px;font-weight:300">Chart Title</div>
      <svg style="position:absolute;left:8px;top:32px" width="134" height="86" viewBox="0 0 134 86">
        <g stroke="#e3e7e7" stroke-width=".4"><line x1="10" y1="10" x2="130" y2="10"/><line x1="10" y1="24" x2="130" y2="24"/><line x1="10" y1="38" x2="130" y2="38"/><line x1="10" y1="52" x2="130" y2="52"/><line x1="10" y1="66" x2="130" y2="66"/></g>
        <g font-size="3" fill="#8c9796" font-family="Lexend"><text x="3" y="11">5</text><text x="3" y="25">4</text><text x="3" y="39">3</text><text x="3" y="53">2</text><text x="3" y="67">1</text></g>
        <polyline points="20,26 50,48 80,30 110,52 128,20" fill="none" stroke="#0d4f45" stroke-width="1"/>
        <polyline points="20,50 50,30 80,52 110,28 128,40" fill="none" stroke="#19b38a" stroke-width="1"/>
        <g font-size="3" fill="#8c9796" font-family="Lexend" text-anchor="middle"><text x="25" y="76">Category 1</text><text x="55" y="76">Category 2</text><text x="85" y="76">Category 3</text><text x="115" y="76">Category 4</text></g>
      </svg>
      <p class="p" style="left:150px;top:32px;width:76px">Our team plans each project with care, from the first brief to the final review. We listen closely, set clear goals and share progress at every step, so clients always know where things stand and what comes next.</p>
      <p class="p" style="left:150px;top:70px;width:76px">Our team plans each project with care, from the first brief to the final review. We listen closely, set clear goals and share progress at every step, so clients always know where things stand and what comes next.</p>
    </article>

    <article class="slide std">
      <div class="st" style="font-weight:400">Pricing <b>table</b></div>
      <table class="tbl">
        <tr><th></th><th>A</th><th>B</th><th>C</th><th>D</th></tr>
        <tr><td>Content A</td><td>$47,000</td><td>$30</td><td>$40</td><td>$20</td></tr>
        <tr><td>Content B</td><td>$47,000</td><td>$54,500</td><td>$76,000</td><td>$80,000</td></tr>
        <tr><td>Content C</td><td>4500</td><td>40000</td><td>$6,000</td><td>$20,000</td></tr>
        <tr><td>Content D</td><td>$4000</td><td>$400</td><td>$400</td><td>$1,200</td></tr>
        <tr><td>Content E</td><td>$40</td><td>$600</td><td>$1,000</td><td>$5,400</td></tr>
      </table>
    </article>

    <article class="slide std">
      <div class="st" style="font-weight:400">Our <b>client</b></div>
      <div class="client" style="left:30px;top:32px"><i></i>Brightlane</div><div class="client" style="left:62px;top:32px"><i></i>Brightlane</div><div class="client" style="left:94px;top:32px"><i></i>Brightlane</div>
      <div class="client" style="left:30px;top:52px"><i></i>Brightlane</div><div class="client" style="left:62px;top:52px"><i></i>Brightlane</div><div class="client" style="left:94px;top:52px"><i></i>Brightlane</div>
      <div class="client" style="left:30px;top:72px"><i></i>Brightlane</div><div class="client" style="left:62px;top:72px"><i></i>Brightlane</div><div class="client" style="left:94px;top:72px"><i></i>Brightlane</div>
      <div class="client" style="left:30px;top:92px"><i></i>Brightlane</div><div class="client" style="left:62px;top:92px"><i></i>Brightlane</div><div class="client" style="left:94px;top:92px"><i></i>Brightlane</div>
      <svg style="position:absolute;left:140px;top:40px" width="12" height="70"><g fill="#0d4f45"><circle cx="6" cy="6" r="5"/><circle cx="6" cy="27" r="5"/><circle cx="6" cy="48" r="5"/></g></svg>
      <p class="p" style="left:156px;top:40px;width:66px">We listen closely, set clear goals and share progress at every step.</p>
      <p class="p" style="left:156px;top:61px;width:66px">We listen closely, set clear goals and share progress at every step.</p>
      <p class="p" style="left:156px;top:82px;width:66px">We listen closely, set clear goals and share progress at every step.</p>
    </article>

    <article class="slide std">
      <div class="st" style="font-weight:400">Our <b>timeline</b></div>
      <p class="p c" style="left:20px;top:20px;width:200px">Our team plans each project with care, from the first brief to the final review. We listen closely, set clear goals and share progress at every step, so clients always know where things stand and what comes next. We listen closely, set clear goals and share progress at every step.</p>
      <div style="position:absolute;left:119px;top:58px;width:.6px;height:62px;background:var(--ink)"></div>
      <div class="gbox" style="left:110px;top:56px;width:18px;height:4px"></div>
      <div class="lbl" style="position:absolute;left:52px;top:80px;text-transform:none;color:var(--ink);font-size:4px">Your Subtitle Here</div>
      <p class="p r" style="left:30px;top:87px;width:82px">We listen closely, set clear goals and share progress at every step.</p>
      <div class="card" style="left:126px;top:68px;width:66px;height:48px"><div class="ph" style="left:0;top:0;width:66px;height:26px" role="img" aria-label="Colleagues at a laptop"></div><div class="lbl" style="position:absolute;left:18px;top:30px;text-transform:none;font-size:3.4px">March</div></div>
    </article>

    <article class="slide std">
      <div style="position:absolute;left:119px;top:0;width:.6px;height:120px;background:var(--ink)"></div>
      <div class="card" style="left:22px;top:12px;width:88px;height:50px"><div class="ph" style="left:30px;top:0;width:58px;height:26px" role="img" aria-label="Business meeting photo"></div><div class="lbl" style="position:absolute;left:30px;top:30px;text-transform:none;font-size:3.4px">April</div></div>
      <div class="lbl" style="position:absolute;left:126px;top:28px;text-transform:none;color:var(--ink);font-size:4px">Your Subtitle Here</div>
      <p class="p" style="left:126px;top:35px;width:84px">Our team plans each project with care, from the first brief to the final review. We listen closely, set clear goals and share progress at every step, so clients always know where things stand and what comes next.</p>
      <div class="lbl" style="position:absolute;left:68px;top:72px;text-transform:none;color:var(--ink);font-size:4px">Your Subtitle Here</div>
      <p class="p r" style="left:28px;top:79px;width:84px">Our team plans each project with care, from the first brief to the final review. We listen closely, set clear goals and share progress at every step, so clients always know where things stand and what comes next.</p>
      <div class="card" style="left:130px;top:66px;width:90px;height:50px"><div class="ph" style="left:0;top:0;width:60px;height:26px" role="img" aria-label="Team meeting photo"></div><div class="lbl" style="position:absolute;left:20px;top:30px;text-transform:none;font-size:3.4px">May</div></div>
    </article>

    <article class="slide std">
      <div style="position:absolute;left:119px;top:0;width:.6px;height:92px;background:var(--ink)"></div>
      <div class="card" style="left:22px;top:12px;width:88px;height:50px"><div class="ph" style="left:0;top:0;width:88px;height:26px" role="img" aria-label="Colleagues working photo"></div><div class="lbl" style="position:absolute;left:24px;top:30px;text-transform:none;font-size:3.4px">June</div></div>
      <div class="lbl" style="position:absolute;left:126px;top:28px;text-transform:none;color:var(--ink);font-size:4px">Your Subtitle Here</div>
      <p class="p" style="left:126px;top:35px;width:84px">Our team plans each project with care, from the first brief to the final review. We listen closely, set clear goals and share progress at every step, so clients always know where things stand and what comes next.</p>
      <div class="gbox" style="left:110px;top:88px;width:18px;height:4px"></div>
      <div class="lbl" style="position:absolute;left:102px;top:95px;text-transform:none;color:var(--ink);font-size:4px">End Timeline</div>
      <p class="p c" style="left:20px;top:103px;width:200px">We listen closely, set clear goals and share progress at every step, so clients always know where things stand.</p>
    </article>

    <article class="slide std">
      <div class="st">Client <b>testimonial</b></div>
      <div class="tcard" style="left:34px"><div class="av" role="img" aria-label="Client portrait"></div><div class="stars">★★★★★</div><p class="p">We listen closely, set clear goals and share progress at every step.</p><div class="nm">Nina Rowe</div></div>
      <div class="tcard on" style="left:93px;width:64px"><div class="av" role="img" aria-label="Client portrait"></div><div class="stars">★★★★★</div><p class="p">We listen closely, set clear goals and share progress at every step.</p><div class="nm">Nina Rowe</div></div>
      <div class="tcard" style="left:164px"><div class="av" role="img" aria-label="Client portrait"></div><div class="stars">★★★★★</div><p class="p">We listen closely, set clear goals and share progress at every step.</p><div class="nm">Ezra Hale</div></div>
    </article>

    <article class="slide std">
      <div class="ph" style="left:26px;top:16px;width:70px;height:80px" role="img" aria-label="Portrait of a smiling client"></div>
      <div class="gbox" style="left:26px;top:88px;width:172px;height:26px"></div>
      <div class="lbl" style="position:absolute;left:112px;top:24px;color:var(--ink);font-size:5px">Testimonial</div>
      <div style="position:absolute;left:112px;top:30px;font-size:10px;font-weight:700;color:var(--ink)">“</div>
      <p class="p" style="left:112px;top:44px;width:112px">Our team plans each project with care, from the first brief to the final review. We listen closely, set clear goals and share progress at every step, so clients always know where things stand and what comes next. We listen closely, set clear goals and share progress at every step.</p>
      <p class="p" style="left:90px;top:96px;width:100px;color:#cfe3df">Client name and company role sit here in a short line.</p>
    </article>

    <article class="slide std">
      <div class="st">3D <b>infographics</b></div>
      <svg style="position:absolute;left:0;top:0" width="238" height="133" viewBox="0 0 238 133">
        <g><rect x="118" y="100" width="14" height="12" fill="#0d4f45"/><rect x="136" y="86" width="14" height="26" fill="#1f2b2a"/><rect x="154" y="72" width="14" height="40" fill="#1f2b2a"/><rect x="172" y="58" width="14" height="54" fill="#8c9796"/><rect x="190" y="40" width="14" height="72" fill="#0d4f45"/></g>
        <polygon points="184,40 210,40 197,20" fill="#0d4f45"/>
        <g font-size="3.4" font-weight="600" fill="#1f2b2a" font-family="Lexend" text-anchor="end"><text x="96" y="101">Step 01</text><text x="110" y="85">Step 02</text><text x="124" y="71">Step 03</text><text x="138" y="57">Step 04</text><text x="152" y="39">Step 05</text></g>
      </svg>
      <p class="p r" style="left:40px;top:103px;width:56px">Short note about this step here.</p>
      <p class="p r" style="left:54px;top:87px;width:56px">Short note about this step here.</p>
      <p class="p r" style="left:68px;top:73px;width:56px">Short note about this step here.</p>
      <p class="p r" style="left:82px;top:59px;width:56px">Short note about this step here.</p>
      <p class="p r" style="left:96px;top:41px;width:56px">Short note about this step here.</p>
    </article>

    <article class="slide std">
      <div class="st">Wristwatch <b>mockup</b></div>
      <p class="p" style="left:22px;top:24px;width:104px">Our team plans each project with care, from the first brief to the final review. We listen closely, set clear goals and share progress at every step, so clients always know where things stand and what comes next.</p>
      <p class="p" style="left:22px;top:56px;width:104px">Our team plans each project with care, from the first brief to the final review. We listen closely, set clear goals and share progress at every step, so clients always know where things stand and what comes next.</p>
      <svg style="position:absolute;left:30px;top:92px" width="90" height="22" viewBox="0 0 90 22">
        <g fill="none" stroke-width="2"><circle cx="10" cy="11" r="8" stroke="#e3e7e7"/><circle cx="10" cy="11" r="8" stroke="#0d4f45" stroke-dasharray="33 50"/><circle cx="45" cy="11" r="8" stroke="#e3e7e7"/><circle cx="45" cy="11" r="8" stroke="#0d4f45" stroke-dasharray="37 50"/><circle cx="80" cy="11" r="8" stroke="#e3e7e7"/><circle cx="80" cy="11" r="8" stroke="#0d4f45" stroke-dasharray="43 50"/></g>
      </svg>
      <div class="ph" style="left:140px;top:24px;width:70px;height:88px;border-radius:14px;background:linear-gradient(135deg,#b8bde0,#6f78a8)" role="img" aria-label="Smartwatch product photo"></div>
    </article>

    <article class="slide std">
      <div class="st">Phone <b>mockup</b></div>
      <p class="p" style="left:22px;top:22px;width:94px">Our team plans each project with care, from the first brief to the final review. We listen closely, set clear goals and share progress at every step, so clients always know where things stand and what comes next. We listen closely, set clear goals and share progress at every step.</p>
      <p class="p" style="left:22px;top:66px;width:94px">Our team plans each project with care, from the first brief to the final review. We listen closely, set clear goals and share progress at every step, so clients always know where things stand and what comes next.</p>
      <div class="ph" style="left:124px;top:36px;width:98px;height:62px;border-radius:8px;transform:rotate(-14deg)" role="img" aria-label="Smartphone showing a business photo"></div>
    </article>

    <article class="slide std">
      <div class="st">Screen <b>mockup</b></div>
      <div class="ph" style="left:30px;top:30px;width:76px;height:56px;border-radius:3px" role="img" aria-label="Laptop screen showing a team photo"></div>
      <p class="p" style="left:148px;top:26px;width:78px">Our team plans each project with care, from the first brief to the final review. We listen closely, set clear goals and share progress at every step, so clients always know where things stand and what comes next.</p>
      <p class="p" style="left:148px;top:66px;width:78px">Our team plans each project with care, from the first brief to the final review. We listen closely, set clear goals and share progress at every step, so clients always know where things stand and what comes next.</p>
    </article>

    <article class="slide std">
      <div class="ph" style="left:0;top:0;width:110px;height:122px" role="img" aria-label="Businessman using a smartphone"></div>
      <div class="st" style="left:118px">Get in <b>touch</b></div>
      <svg style="position:absolute;left:128px;top:28px" width="8" height="80" viewBox="0 0 8 80"><line x1="4" y1="0" x2="4" y2="56" stroke="#8c9796" stroke-width=".4"/><g fill="#0d4f45"><path d="M4 4c-1.6 0-2.6 1.2-2.6 2.5C1.4 8.3 4 11 4 11s2.6-2.7 2.6-4.5C6.6 5.2 5.6 4 4 4z"/><path d="M4 28c-1.6 0-2.6 1.2-2.6 2.5C1.4 32.3 4 35 4 35s2.6-2.7 2.6-4.5C6.6 29.2 5.6 28 4 28z"/><rect x="2" y="58" width="4" height="6" rx="1"/><rect x="1.5" y="70" width="5" height="4"/></g></svg>
      <p class="p" style="left:140px;top:30px;width:80px;color:var(--ink)">Office<br>48 Elm Row</p>
      <p class="p" style="left:140px;top:55px;width:80px;color:var(--ink)">Regional Office<br>12 Quay St</p>
      <p class="p" style="left:140px;top:86px;width:80px;color:var(--ink)">0123 456 789</p>
      <p class="p" style="left:140px;top:98px;width:80px;color:var(--ink)">hello@novaridge.co</p>
    </article>

    <article class="slide thanks">
      <div class="brand">NOVARIDGE</div>
      <h3>Thank you</h3>
    </article>

    <article class="slide">
      <div class="iconset" style="top:8px"><h4>General</h4>○□△◇☆♡✉✎⌂⚙☰✓✕⌕☏✆⚑⌚☀☁☂♫✂✈⌘⚐○□△◇☆♡✉✎⌂⚙☰✓✕⌕☏✆⚑⌚☀☁☂♫✂✈⌘⚐○□△◇☆♡✉✎⌂⚙☰✓✕⌕☏✆<h4>Electronics</h4>☏⌚⌨✆▣▤▥▦▧▨◫◧◨☏⌚⌨✆▣▤▥▦▧▨◫◧◨☏⌚⌨✆▣▤▥▦▧▨◫◧◨▣▤</div>
    </article>

    <article class="slide">
      <div class="iconset" style="top:6px"><h4>E-commerce</h4>☐☑✓✚✦◈◉◎☆♡⌂☐☑✓✚✦◈◉◎☆♡⌂☐☑✓✚✦◈◉◎☆<h4>Web</h4>⌕⚙☰✉✎⌂⌘☁⚑◐◑◒⌕⚙☰✉✎⌂⌘☁⚑◐◑◒⌕⚙☰✉✎<h4>Location</h4>⚲⚐⚑⌖◎⊕⚲⚐⚑⌖◎⊕⚲⚐⚑⌖◎⊕⚲⚐<h4>Arrows</h4>←↑→↓↔↕↖↗↘↙⇐⇒⇑⇓←↑→↓↔↕↖↗↘↙⇐⇒</div>
    </article>

    <article class="slide">
      <div class="iconset" style="top:8px"><h4>Weather</h4>☀☁☂☃☄★☾◐◑◒◓●○☀☁☂☃☄★☾◐◑◒◓<h4>Miscellaneous</h4>♠♣♥♦♪♫✂✈✉✎✏✐✑✒✓✔✕✖✗✘♠♣♥♦♪♫✂✈✉✎✏✐✑✒✓✔✕✖✗✘♠♣♥♦♪♫✂✈✉✎✏✐✑</div>
    </article>

  </section>
</main>
</body>
</html>
```